New Agency Branding - Logo & Business Card

Project Description

ZUM is a creative agency that crafts memorable product experiences through meaningful design. By channeling the needs of the business and its customers, we are able to construct solutions that are elegant yet effective, powerful yet playful, and familiar yet stimulating.

In addition to our focus towards creating excellent products, we firmly believe that building a strong company culture is paramount. Our values revolve around building an environment that is passionate, supportive, collaborative, curious, humorous, and healthy. The ZUM team is relatively small, and we intend on keep this family tight-knit. We take great care in deciding who we work with and what we work on.

What we’re looking for is a designer who is willing to take on the challenge of helping us visually define and express the ZUM brand. We must comfortably occupy the consumer, commercial, and enterprise sectors. This means looking professional without sacrificing charm. We’re passionate about design and we care about people.

Deliverables

Logo

The first exercise would be to create the ZUM LOGO by referencing the concept that is attached (filename: ZUM Concept Logo). We like the idea of utilizing negative space, but are open to other suggestions. In terms of color, we’ve been flirting with the idea of purple as the primary color, but are again open to other explorations. The logo should be bold, professional, playful, and versatile (it should look just as crisp blown up on a website as it would on a contract).

Accepted Format(s): Adobe Illustrator (.ai) 

Business Card

The second exercise would be to design a business card utilizing the logo. The shape can be standard or square (single our double-sided), and must include the following:

• ZUM LOGO
• Tagline: "human experiences, designed"
• First and Last Name
• Job Role
• Contact Information (email address and phone number)
• Website URL

In terms of typography, we’d like to see considered pairings that compliment the logo, are legible, and can cohesively translate to other mediums (i.e. the ZUM website).

Accepted Format(s): Adobe Photoshop (.psd) OR Adobe Illustrator (.ai)

Style Guide

Finally, we’d like to have the brand defined and presented in a style guide. This would include the full color palette (primary color, secondary color, etc.) and font usage. In addition, we’d like to see rationale clearly communicated for the decisions made.

Visual References

Companies that inspire us:

morrow+venn
http://www.morrowvenn.example/story/morrow-venn/

BRISK
http://www.briskstudio.example

NestHop
https://www.nesthop.example

Fundlark
https://www.fundlark.example

Target Market(s)

Startups, Small to Mid Sized Businesses, Consultant Businesses

Industry/Entity Type

Design Agency

Contact Information for Business Card

FRONT: ZUM LOGO on White background

BACK: Tag line "human experiences, designed", name (i.e. John Doe), job role (i.e. Director, Product Development), phone number, email address, and website. The background color could be a solid color although we are open to suggestions.

Logo Text

ZUM

Font styles to use
Sans Serif

Colors
b768aa
a54499
d2a4cc
876aae
6b449b

Requirements
Must have
• A sense of playfulnesses, charm, excitement, and energy.
• Clean and minimal design
• Avoid using icons for contact information
• NOTE: Not all of the purples that have been chosen must be used. These are only suggestions.

```html
<!DOCTYPE html>
<html lang="en">
<head>
<meta charset="utf-8">
<title>ZUM — Business Card</title>
<link href="https://fonts.googleapis.com/css2?family=Quicksand:wght@300;400;500&display=swap" rel="stylesheet">
<style>
  :root {
    --page-bg: #ecebef;
    --purple-deep: #6b449b;
    --purple-main: #876aae;
    --purple-light: #b9a3d6;
    --purple-soft: #c9b6e0;
    --card-white: #fbfbfc;
    --ink: #2b2b33;
    --white: #ffffff;
  }
  * { margin: 0; padding: 0; box-sizing: border-box; }
  html, body {
    width: 771px;
    height: 1200px;
    overflow: hidden;
    background: var(--page-bg);
    font-family: "Quicksand", sans-serif;
  }
  .canvas {
    position: relative;
    width: 771px;
    height: 1200px;
  }
  .card {
    position: absolute;
    left: 76px;
    width: 620px;
    height: 354px;
    border-radius: 4px;
    box-shadow: 0 10px 28px rgba(40, 30, 60, 0.18);
    overflow: hidden;
  }
  /* front side */
  .card--front {
    top: 110px;
    background: radial-gradient(ellipse at 62% 40%, var(--purple-soft) 0%, var(--purple-main) 55%, var(--purple-deep) 100%);
    color: var(--white);
  }
  .card--front .brand-name {
    position: absolute;
    left: 0; right: 0;
    top: 100px;
    text-align: center;
    font-size: 78px;
    font-weight: 500;
    letter-spacing: 6px;
    line-height: 1;
  }
  .card--front .tagline {
    position: absolute;
    left: 0; right: 0;
    top: 214px;
    text-align: center;
    font-size: 27px;
    font-weight: 300;
    letter-spacing: 0.5px;
  }
  /* back side */
  .card--back {
    top: 676px;
    background: radial-gradient(ellipse at 50% 40%, var(--white) 0%, var(--card-white) 60%, #eeeef1 100%);
    color: var(--ink);
  }
  .card--back .brand-name {
    position: absolute;
    left: 40px;
    top: 200px;
    font-size: 66px;
    font-weight: 500;
    letter-spacing: 5px;
    color: var(--purple-light);
    line-height: 1;
  }
  .card--back .divider {
    position: absolute;
    left: 262px;
    top: 120px;
    width: 1.5px;
    height: 150px;
    background: var(--purple-light);
  }
  .card--back .details {
    position: absolute;
    left: 286px;
    top: 92px;
  }
  .person-name {
    font-size: 26px;
    font-weight: 400;
    line-height: 1.1;
  }
  .job-title {
    font-size: 15px;
    font-weight: 400;
    color: var(--purple-light);
    margin-top: 4px;
  }
  .contact-list {
    list-style: none;
    margin-top: 18px;
  }
  .contact-list li {
    display: flex;
    align-items: center;
    gap: 9px;
    font-size: 16px;
    font-weight: 400;
    line-height: 1.7;
  }
  .contact-list svg {
    width: 12px;
    height: 12px;
    fill: var(--purple-light);
    flex: none;
  }
</style>
</head>
<body>
<main class="canvas">
  <section class="card card--front" aria-label="Card front">
    <div class="brand-name">ZUM</div>
    <p class="tagline">human experiences, designed</p>
  </section>

  <section class="card card--back" aria-label="Card back">
    <div class="brand-name">ZUM</div>
    <div class="divider"></div>
    <div class="details">
      <h1 class="person-name">Your Name</h1>
      <p class="job-title">Job title</p>
      <ul class="contact-list">
        <li>
          <svg viewBox="0 0 12 12" aria-hidden="true"><path d="M1 3.5C1 2 2.5 1 6 1s5 1 5 2.5V5H8.5V4h-5v1H1z M2 6h8l1 5H1z"/></svg>
          000 000 0000
        </li>
        <li>
          <svg viewBox="0 0 12 12" aria-hidden="true"><path d="M1 2.5h10v7H1z M1.5 3l4.5 3.5L10.5 3" stroke="#fff" stroke-width="0.8"/></svg>
          youremail@zum.example
        </li>
        <li>
          <svg viewBox="0 0 12 12" aria-hidden="true"><circle cx="6" cy="6" r="5"/><path d="M1 6h10M6 1v10M2.5 3.5h7M2.5 8.5h7" stroke="#fff" stroke-width="0.7" fill="none"/></svg>
          websiteurl.example
        </li>
      </ul>
    </div>
  </section>
</main>
</body>
</html>
```